Sports coaching website.

Hi there web designers,

We need a modern fully functional website to set us apart from our competition. The website will be information based with pictures and videos provided by us. The website must include members log in where they can pay for sessions directly online and subscribe to direct debit.

Target Market(s)

parents/teachers/schools/community/children.

Number of Pages Required

5+ page

Font styles to use
Sans Serif

Colors
acd037
3176b5
ffffff
000000
919191
f37122

Requirements
Must have
• Pictures, be modern, fully functional, must be clear, bold, e-basket, log-in.

```html
<!DOCTYPE html>
<html lang="en">
<head>
<meta charset="utf-8">
<title>Fieldcraft Sports</title>
<link rel="stylesheet" href="https://fonts.googleapis.com/css2?family=Arimo:wght@400;700&family=Open+Sans:wght@400;600;700&display=swap">
<style>
:root{
  --green:#acd037;
  --blue:#3176b5;
  --white:#ffffff;
  --black:#000000;
  --grey:#919191;
  --orange:#f37122;
  --ink:#222222;
  --text:#6e6e6e;
  --band:#efefef;
  --footer:#1f1f1f;
}
*{margin:0;padding:0;box-sizing:border-box}
html,body{width:1200px;height:2941px;overflow:hidden}
body{position:relative;background:var(--white);font-family:"Open Sans",Arial,sans-serif;color:var(--text)}
.abs{position:absolute}
.heading{position:absolute;left:0;width:1200px;text-align:center;font-family:"Arimo",Arial,sans-serif;font-weight:700;font-size:25px;color:var(--ink);letter-spacing:.3px}
.heading.on-orange{color:var(--white)}
.photo{position:absolute}

/* header */
.top-line{left:0;top:0;width:1200px;height:5px;background:var(--blue)}
.header{left:0;top:5px;width:1200px;height:83px;background:var(--white)}
.brand{left:100px;top:22px;width:150px;font-family:"Arimo",Arial,sans-serif;font-weight:700;font-size:24px;line-height:1.1;color:var(--black);z-index:3}
.contact-item{top:15px;font-size:14px;color:var(--ink);display:flex;align-items:center;gap:8px}
.contact-item .ico{width:26px;height:26px;border-radius:50%;background:var(--green);display:flex;align-items:center;justify-content:center}
.login{left:958px;top:12px;width:142px;height:34px;background:var(--green);color:var(--white);font-size:12px;font-weight:700;display:flex;align-items:center;justify-content:center;gap:6px}
.nav{top:62px;left:332px;display:flex;gap:25px;font-family:"Arimo",Arial,sans-serif;font-weight:700;font-size:13px;color:var(--ink)}
.nav .active{color:var(--green)}

/* hero */
.hero{left:0;top:88px;width:1200px;height:426px;background:linear-gradient(180deg,#6f6a62 0%,#8a5e4d 38%,#4d7f3a 56%,#2f6f2a 100%)}
.hero-title{left:577px;top:234px;font-family:"Arimo",Arial,sans-serif;font-weight:700;font-size:48px;color:var(--white)}
.hero-sub{left:579px;top:290px;font-size:22px;color:var(--white)}
.hero-btn{left:577px;top:335px;width:198px;height:40px;background:var(--green);color:var(--white);font-size:14px;font-weight:700;display:flex;align-items:center;justify-content:center}
.dots{left:545px;top:462px;display:flex;gap:6px}
.dots span{width:22px;height:4px;background:var(--white)}
.dots span:first-child{background:var(--blue)}

/* what we do */
.intro{left:210px;top:608px;width:780px;text-align:center;font-size:12px;line-height:22px}
.feature{position:absolute;top:682px;width:240px;text-align:center}
.feature .ring{width:138px;height:138px;margin:0 auto;display:block}
.feature h3{margin-top:26px;font-family:"Arimo",Arial,sans-serif;font-size:14px;color:var(--ink)}
.feature p{margin-top:12px;font-size:12px;line-height:20px;padding:0 8px}
.feature .more{margin-top:14px;font-size:12px;font-weight:700;color:var(--green)}

/* services */
.services{left:0;top:1008px;width:1200px;height:488px;background:var(--band)}
.service{position:absolute;top:1106px;width:316px}
.service .photo{position:relative;width:316px;height:196px;border:4px solid var(--white);box-shadow:0 1px 4px rgba(0,0,0,.15)}
.service h3{margin-top:20px;font-family:"Arimo",Arial,sans-serif;font-size:16px;color:var(--ink)}
.service p{margin-top:10px;font-size:12px;line-height:21px}
.service .more{margin-top:10px;font-size:12px;font-weight:700;color:var(--green)}

/* testimonials */
.testimonials{left:0;top:1496px;width:1200px;height:408px;background:var(--orange)}
.video{position:absolute;top:1596px;width:304px;height:180px;background:var(--black)}
.video .photo{left:0;top:14px;width:304px;height:152px}
.play{position:absolute;left:132px;top:68px;width:40px;height:40px;border-radius:50%;background:var(--black);display:flex;align-items:center;justify-content:center}
.person{position:absolute;top:1794px;display:flex;align-items:center;gap:14px}
.avatar{width:70px;height:70px;border-radius:50%;border:4px solid var(--white)}
.person b{display:block;font-family:"Arimo",Arial,sans-serif;font-size:17px;color:var(--white)}
.person span{font-size:12px;color:var(--white)}
.arrow{position:absolute}

/* events */
.event{position:absolute;top:2012px;width:240px}
.event .photo{position:relative;width:240px;height:143px}
.date{position:absolute;right:0;bottom:0;background:var(--blue);color:var(--white);font-size:11px;padding:4px 8px;display:flex;gap:5px;align-items:center}
.event h3{margin-top:16px;font-family:"Arimo",Arial,sans-serif;font-size:16px;color:var(--ink)}
.event p{margin-top:8px;font-size:12px;line-height:21px}
.event .btns{margin-top:14px;display:flex;justify-content:space-between}
.btn{width:116px;height:32px;display:flex;align-items:center;justify-content:center;color:var(--white);font-size:11px;font-weight:700}
.btn.book{background:var(--green)}
.btn.read{background:var(--orange)}

/* gallery */
.gallery{left:0;top:2366px;width:1200px;height:274px;background:var(--band)}
.gallery-item{position:absolute;top:2466px;width:190px;height:126px;border:3px solid var(--white)}

/* footer */
.footer{left:0;top:2640px;width:1200px;height:301px;background:var(--footer);border-top:5px solid var(--blue)}
.foot-brand{left:120px;top:2730px;width:180px;font-family:"Arimo",Arial,sans-serif;font-weight:700;font-size:28px;line-height:1.1;color:var(--white)}
.foot-head{top:2674px;font-family:"Arimo",Arial,sans-serif;font-weight:700;font-size:16px;color:var(--white)}
.foot-links{left:374px;top:2716px;font-size:12px;line-height:19px;color:#d8d8d8;list-style:none}
.foot-text{font-size:12px;line-height:20px;color:#d8d8d8}
.email-field{left:561px;top:2770px;width:232px;height:32px;background:var(--white);font-size:11px;color:var(--grey);padding:9px 12px}
.subscribe{left:561px;top:2814px;width:102px;height:34px;border:2px solid var(--white);color:var(--white);font-size:12px;font-weight:700;display:flex;align-items:center;justify-content:center}
.c-row{left:872px;display:flex;gap:18px;font-size:12px;line-height:18px;color:#d8d8d8}
.c-row svg{flex:none;margin-top:2px}
.foot-rule{left:98px;top:2874px;width:1004px;height:1px;background:#3a3a3a}
.copyright{left:100px;top:2896px;font-size:11px;color:#d8d8d8}
.socials{left:958px;top:2888px;display:flex;gap:8px}
.socials span{width:32px;height:32px;border-radius:50%;border:2px solid var(--white)}
</style>
</head>
<body>

<!-- Header -->
<div class="abs top-line"></div>
<header class="abs header">
  <div class="abs contact-item" style="left:564px">
    <span class="ico"><svg width="14" height="14" viewBox="0 0 24 24"><path fill="#fff" d="M6.6 10.8a15 15 0 0 0 6.6 6.6l2.2-2.2c.3-.3.7-.4 1-.2 1.1.4 2.3.6 3.6.6.6 0 1 .4 1 1V20c0 .6-.4 1-1 1A17 17 0 0 1 3 4c0-.6.4-1 1-1h3.5c.6 0 1 .4 1 1 0 1.3.2 2.5.6 3.6.1.3 0 .7-.2 1z"/></svg></span>
    1 800 555 014
  </div>
  <div class="abs contact-item" style="left:720px">
    <span class="ico"><svg width="14" height="14" viewBox="0 0 24 24"><path fill="#fff" d="M3 5h18v14H3z"/><path fill="none" stroke="#acd037" stroke-width="2" d="M3 6l9 7 9-7"/></svg></span>
    info@fieldcraftsports.com
  </div>
  <div class="abs login"><svg width="12" height="12" viewBox="0 0 24 24"><circle cx="12" cy="8" r="5" fill="#fff"/><path fill="#fff" d="M3 22c0-5 4-8 9-8s9 3 9 8z"/></svg>MEMBER LOGIN</div>
  <nav class="abs nav">
    <span class="active">HOME</span><span>ABOUT FCS</span><span>SCHOOLS</span><span>SESSIONS</span><span>WORKSHOPS</span><span>CHARITY/COMMUNITY</span><span>CONTACT</span>
    <svg width="14" height="14" viewBox="0 0 24 24"><circle cx="10" cy="10" r="7" fill="none" stroke="#222" stroke-width="3"/><path d="M15 15l6 6" stroke="#222" stroke-width="3"/></svg>
  </nav>
</header>
<div class="abs brand">FIELDCRAFT<br>SPORTS</div>

<!-- Hero -->
<section class="abs hero" role="img" aria-label="Photo of a young footballer in a blue kit dribbling a ball past cones on an artificial pitch"></section>
<h1 class="abs hero-title">FIELDCRAFT SPORTS</h1>
<p class="abs hero-sub">We are a sports coaching center</p>
<div class="abs hero-btn">GET MORE INFO &gt;&gt;</div>
<div class="abs dots"><span></span><span></span><span></span><span></span></div>

<!-- What we do -->
<h2 class="heading" style="top:566px">WHAT WE DO</h2>
<p class="abs intro">At vero eos et accusamus et iusto odio dignissimos ducimus qui blanditiis praesentium voluptatum deleniti atque corrupti quos dolores et quas molestias excepturi sint occaecati cupiditate non provident, similique sunt in culpa qui officia deserunt mollitia animi, id est</p>

<div class="feature" style="left:92px">
  <svg class="ring" viewBox="0 0 138 138"><circle cx="69" cy="69" r="64" fill="none" stroke="#3176b5" stroke-width="7"/><path d="M69 2v10M69 126v10M2 69h10M126 69h10" stroke="#fff" stroke-width="4"/><path d="M55 40h28l-6 22H61z" fill="#3176b5"/><circle cx="69" cy="80" r="16" fill="#3176b5"/><circle cx="69" cy="80" r="7" fill="#fff"/></svg>
  <h3>SPORTS EDUCATION</h3>
  <p>Nam libero tempore, cum soluta nob is est eligendi optio cumque nihil impedit quo minus id quod maxime</p>
  <div class="more">READ MORE &gt;&gt;</div>
</div>
<div class="feature" style="left:350px">
  <svg class="ring" viewBox="0 0 138 138"><circle cx="69" cy="69" r="64" fill="none" stroke="#3176b5" stroke-width="7"/><path d="M69 2v10M69 126v10M2 69h10M126 69h10" stroke="#fff" stroke-width="4"/><circle cx="69" cy="69" r="28" fill="#3176b5"/><circle cx="69" cy="69" r="24" fill="#fff"/><path d="M69 58l10 7-4 12H63l-4-12z" fill="#3176b5"/><path d="M69 46v12M79 65l12-4M75 77l7 10M63 77l-7 10M59 65l-12-4" stroke="#3176b5" stroke-width="3"/></svg>
  <h3>TRAINING &amp; TECHNOLOGY</h3>
  <p>Nam libero tempore, cum soluta nob is est eligendi optio cumque nihil impedit quo minus id quod maxime</p>
  <div class="more">READ MORE &gt;&gt;</div>
</div>
<div class="feature" style="left:607px">
  <svg class="ring" viewBox="0 0 138 138"><circle cx="69" cy="69" r="64" fill="none" stroke="#3176b5" stroke-width="7"/><path d="M69 2v10M69 126v10M2 69h10M126 69h10" stroke="#fff" stroke-width="4"/><g transform="rotate(-45 69 69)" fill="#3176b5"><rect x="50" y="65" width="38" height="8"/><rect x="38" y="50" width="10" height="38" rx="2"/><rect x="90" y="50" width="10" height="38" rx="2"/><rect x="30" y="57" width="7" height="24" rx="2"/><rect x="101" y="57" width="7" height="24" rx="2"/></g></svg>
  <h3>FITNESS DEVELOPMENT</h3>
  <p>Nam libero tempore, cum soluta nob is est eligendi optio cumque nihil impedit quo minus id quod maxime</p>
  <div class="more">READ MORE &gt;&gt;</div>
</div>
<div class="feature" style="left:865px">
  <svg class="ring" viewBox="0 0 138 138"><circle cx="69" cy="69" r="64" fill="none" stroke="#3176b5" stroke-width="7"/><path d="M69 2v10M69 126v10M2 69h10M126 69h10" stroke="#fff" stroke-width="4"/><path d="M69 36c-10 0-14 8-14 14 0 8 8 18 8 18L46 98l10 6 13-24 13 24 10-6-17-30s8-10 8-18c0-6-4-14-14-14zm0 10c4 0 5 3 5 5 0 3-5 10-5 10s-5-7-5-10c0-2 1-5 5-5z" fill="#3176b5"/></svg>
  <h3>AWARENESS FOR SPORTS</h3>
  <p>Nam libero tempore, cum soluta nob is est eligendi optio cumque nihil impedit quo minus id quod maxime</p>
  <div class="more">READ MORE &gt;&gt;</div>
</div>

<!-- Services -->
<section class="abs services"></section>
<h2 class="heading" style="top:1050px">OUR SERVICES</h2>
<div class="service" style="left:98px">
  <div class="photo" role="img" aria-label="Photo of a smiling girl holding a badminton racket outdoors" style="background:linear-gradient(135deg,#c9a24a,#e9d6a8 50%,#8fa35a)"></div>
  <h3>FINIBUS BONORUM ET MALORUM</h3>
  <p>At vero eos et accusamus et iusto odio dignissimos duci mus qui blanditiis praesentium voluptatum delenitatque corrupti quos olore quas molest.</p>
  <div class="more">READ MORE &gt;&gt;</div>
</div>
<div class="service" style="left:443px">
  <div class="photo" role="img" aria-label="Photo of children sitting on a sports hall floor with a basketball" style="background:linear-gradient(135deg,#c8b49a,#e6ddd0 50%,#a67c52)"></div>
  <h3>FINIBUS BONORUM ET MALORUM</h3>
  <p>At vero eos et accusamus et iusto odio dignissimos duci mus qui blanditiis praesentium voluptatum delenitatque corrupti quos olore quas molest.</p>
  <div class="more">READ MORE &gt;&gt;</div>
</div>
<div class="service" style="left:785px">
  <div class="photo" role="img" aria-label="Photo of a youth football team in red kits huddling under a blue sky" style="background:linear-gradient(180deg,#7fb0e0,#c73a32 55%,#e8e8e8)"></div>
  <h3>FINIBUS BONORUM ET MALORUM</h3>
  <p>At vero eos et accusamus et iusto odio dignissimos duci mus qui blanditiis praesentium voluptatum delenitatque corrupti quos olore quas molest.</p>
  <div class="more">READ MORE &gt;&gt;</div>
</div>

<!-- Testimonials -->
<section class="abs testimonials"></section>
<h2 class="heading on-orange" style="top:1542px">TESTIMONIALS</h2>
<svg class="arrow" style="left:66px;top:1672px" width="16" height="28" viewBox="0 0 16 28"><path d="M14 2L3 14l11 12" fill="none" stroke="#fff" stroke-width="3"/></svg>
<svg class="arrow" style="left:1118px;top:1672px" width="16" height="28" viewBox="0 0 16 28"><path d="M2 2l11 12L2 26" fill="none" stroke="#fff" stroke-width="3"/></svg>

<div class="video" style="left:98px"><div class="photo" role="img" aria-label="Video still of a coach helping a boy with a tennis racket" style="background:linear-gradient(90deg,#7d9a6a,#d9c9b0 50%,#c84c3a)"></div><div class="play"><svg width="14" height="16" viewBox="0 0 14 16"><path d="M2 1l11 7-11 7z" fill="#fff"/></svg></div></div>
<div class="video" style="left:449px"><div class="photo" role="img" aria-label="Video still of a parent and a child in a blue shirt" style="background:linear-gradient(90deg,#e4e0da,#9cc3e6 55%,#d8d8d8)"></div><div class="play"><svg width="14" height="16" viewBox="0 0 14 16"><path d="M2 1l11 7-11 7z" fill="#fff"/></svg></div></div>
<div class="video" style="left:798px"><div class="photo" role="img" aria-label="Video still of a teacher with a group of children in a classroom" style="background:linear-gradient(90deg,#e6e2dc,#bfa58a 50%,#3a3a3a)"></div><div class="play"><svg width="14" height="16" viewBox="0 0 14 16"><path d="M2 1l11 7-11 7z" fill="#fff"/></svg></div></div>

<div class="person" style="left:100px"><div class="avatar" role="img" aria-label="Portrait of John Doe" style="background:#c9a78e"></div><div><b>JOHN DOE</b><span>Teachers</span></div></div>
<div class="person" style="left:451px"><div class="avatar" role="img" aria-label="Portrait of Agnus" style="background:#d7b99a"></div><div><b>AGNUS</b><span>Parents</span></div></div>
<div class="person" style="left:800px"><div class="avatar" role="img" aria-label="Portrait of Peter" style="background:#b98d70"></div><div><b>PETER</b><span>Sports</span></div></div>

<!-- Upcoming events -->
<h2 class="heading" style="top:1952px">UPCOMING EVENTS</h2>
<svg class="arrow" style="left:64px;top:2068px" width="14" height="26" viewBox="0 0 14 26"><path d="M12 2L3 13l9 11" fill="none" stroke="#bdbdbd" stroke-width="3"/></svg>
<svg class="arrow" style="left:1122px;top:2068px" width="14" height="26" viewBox="0 0 14 26"><path d="M2 2l9 11-9 11" fill="none" stroke="#bdbdbd" stroke-width="3"/></svg>

<div class="event" style="left:98px">
  <div class="photo" role="img" aria-label="Photo of a child dribbling through cones on a pitch" style="background:linear-gradient(180deg,#8a6e5a,#3f7a34)"><div class="date"><svg width="10" height="10" viewBox="0 0 10 10"><rect x="0.5" y="1.5" width="9" height="8" fill="none" stroke="#fff"/></svg>31/08/2016</div></div>
  <h3>GIBUS BONORUM MALO</h3>
  <p>Temporibus autem quibusdam et aut offici is debitis aut rerum necessitatibus saepev voluptates repudiandae sint.</p>
  <div class="btns"><span class="btn book">BOOK NOW</span><span class="btn read">READ MORE</span></div>
</div>
<div class="event" style="left:353px">
  <div class="photo" role="img" aria-label="Photo of children sitting together with footballs" style="background:linear-gradient(180deg,#cfc4b4,#6c8fb8)"><div class="date"><svg width="10" height="10" viewBox="0 0 10 10"><rect x="0.5" y="1.5" width="9" height="8" fill="none" stroke="#fff"/></svg>31/08/2016</div></div>
  <h3>GIBUS BONORUM MALO</h3>
  <p>Temporibus autem quibusdam et aut offici is debitis aut rerum necessitatibus saepev voluptates repudiandae sint.</p>
  <div class="btns"><span class="btn book">BOOK NOW</span><span class="btn read">READ MORE</span></div>
</div>
<div class="event" style="left:608px">
  <div class="photo" role="img" aria-label="Photo of a junior football team in red shirts with a referee" style="background:linear-gradient(180deg,#5d7f45,#b8312b 60%,#3a3a3a)"><div class="date"><svg width="10" height="10" viewBox="0 0 10 10"><rect x="0.5" y="1.5" width="9" height="8" fill="none" stroke="#fff"/></svg>31/08/2016</div></div>
  <h3>GIBUS BONORUM MALO</h3>
  <p>Temporibus autem quibusdam et aut offici is debitis aut rerum necessitatibus saepev voluptates repudiandae sint.</p>
  <div class="btns"><span class="btn book">BOOK NOW</span><span class="btn read">READ MORE</span></div>
</div>
<div class="event" style="left:862px">
  <div class="photo" role="img" aria-label="Photo of kids heading a football during a match" style="background:linear-gradient(180deg,#9fb9cf,#4d7f3a)"><div class="date"><svg width="10" height="10" viewBox="0 0 10 10"><rect x="0.5" y="1.5" width="9" height="8" fill="none" stroke="#fff"/></svg>31/08/2016</div></div>
  <h3>GIBUS BONORUM MALO</h3>
  <p>Temporibus autem quibusdam et aut offici is debitis aut rerum necessitatibus saepev voluptates repudiandae sint.</p>
  <div class="btns"><span class="btn book">BOOK NOW</span><span class="btn read">READ MORE</span></div>
</div>

<!-- Gallery -->
<section class="abs gallery"></section>
<h2 class="heading" style="top:2406px">OUR GALLERY</h2>
<svg class="arrow" style="left:64px;top:2516px" width="14" height="26" viewBox="0 0 14 26"><path d="M12 2L3 13l9 11" fill="none" stroke="#bdbdbd" stroke-width="3"/></svg>
<svg class="arrow" style="left:1122px;top:2516px" width="14" height="26" viewBox="0 0 14 26"><path d="M2 2l9 11-9 11" fill="none" stroke="#bdbdbd" stroke-width="3"/></svg>
<div class="gallery-item" style="left:98px;background:linear-gradient(180deg,#e6dfd2,#c9a56e)" role="img" aria-label="Gallery photo of an indoor sports hall session"></div>
<div class="gallery-item" style="left:302px;background:linear-gradient(180deg,#d8cbb5,#b8874e)" role="img" aria-label="Gallery photo of children in a group activity on a hall floor"></div>
<div class="gallery-item" style="left:508px;background:linear-gradient(180deg,#e2d7c3,#c0895a)" role="img" aria-label="Gallery photo of a class group sitting together"></div>
<div class="gallery-item" style="left:710px;background:linear-gradient(180deg,#ddd5c8,#b89160)" role="img" aria-label="Gallery photo of a badminton drill in a gym"></div>
<div class="gallery-item" style="left:912px;background:linear-gradient(180deg,#d6ccbc,#ae8a5c)" role="img" aria-label="Gallery photo of children playing indoor football"></div>

<!-- Footer -->
<footer class="abs footer"></footer>
<div class="abs foot-brand">FIELDCRAFT<br>SPORTS</div>

<div class="abs foot-head" style="left:374px">INFORMATION</div>
<ul class="abs foot-links">
  <li>Home Page</li><li>About FCS</li><li>Schools</li><li>Sessions</li><li>Workshops</li><li>Charity/Community</li><li>Contact</li>
</ul>

<div class="abs foot-head" style="left:561px">NEWSLETTER</div>
<p class="abs foot-text" style="left:561px;top:2716px;width:240px">Register your email address to get information about us</p>
<div class="abs email-field">Email Address</div>
<div class="abs subscribe">SUBSCRIBE</div>

<div class="abs foot-head" style="left:872px">CONTACT US</div>
<div class="abs c-row" style="top:2718px"><svg width="12" height="14" viewBox="0 0 12 16"><path d="M6 0a6 6 0 0 0-6 6c0 5 6 10 6 10s6-5 6-10a6 6 0 0 0-6-6zm0 8.5a2.5 2.5 0 1 1 0-5 2.5 2.5 0 0 1 0 5z" fill="#fff"/></svg><span>Level 3, Marlow House<br>12 Kestrel Lane<br>Brookvale Heights NSW 2190 Australia</span></div>
<div class="abs c-row" style="top:2784px"><svg width="12" height="12" viewBox="0 0 24 24"><path fill="#fff" d="M6.6 10.8a15 15 0 0 0 6.6 6.6l2.2-2.2c.3-.3.7-.4 1-.2 1.1.4 2.3.6 3.6.6.6 0 1 .4 1 1V20c0 .6-.4 1-1 1A17 17 0 0 1 3 4c0-.6.4-1 1-1h3.5c.6 0 1 .4 1 1 0 1.3.2 2.5.6 3.6.1.3 0 .7-.2 1z"/></svg><span>+1 800 555 014</span></div>
<div class="abs c-row" style="top:2816px"><svg width="12" height="10" viewBox="0 0 24 18"><path fill="#fff" d="M0 0h24v18H0z"/><path d="M0 1l12 9 12-9" fill="none" stroke="#1f1f1f" stroke-width="2"/></svg><span>info@fieldcraftsports.com</span></div>

<div class="abs foot-rule"></div>
<p class="abs copyright">Copyrights © 2016, Fieldcraft Sports. All rights reserved.</p>
<div class="abs socials"><span></span><span></span><span></span><span></span></div>

</body>
</html>
```